Design a business card
Business name: Kestrel Yield Consulting
Improving Business Profitibility

- An Overview of the Business & Service:

Business Performance Consulting

- The Target Market: Small to medium-sized business

- Design Specifics:
White card, blue ink, moon eclipse

No Logo

Target Market(s)

Small to medium-sized business

Font styles to use
Sans Serif

```html
<!DOCTYPE html>
<html lang="en">
<head>
<meta charset="utf-8">
<title>Kestrel Yield Consulting – Business Card</title>
<link href="https://fonts.googleapis.com/css2?family=Questrial&family=Exo+2:wght@500&display=swap" rel="stylesheet">
<style>
  :root {
    --page: #ecebe8;
    --card-white: #ffffff;
    --band-light: #4f8ff0;
    --band-dark: #2d58a8;
    --band-mid: #6ea2ee;
    --moon-light: #eef3f8;
    --moon-shade: #d9e1ea;
    --title-blue: #3a5ca6;
    --tag-blue: #5b82c9;
    --ink: #1f1f24;
    --icon-blue: #4a79c8;
  }
  html, body {
    margin: 0;
    width: 1200px;
    height: 1023px;
    overflow: hidden;
    background: var(--page);
  }
  .business-card {
    position: absolute;
    left: 100px;
    top: 221px;
    width: 1000px;
    height: 580px;
    background: var(--card-white);
    overflow: hidden;
    box-shadow: 0 10px 30px rgba(0,0,0,0.18);
    font-family: "Questrial", sans-serif;
    color: var(--ink);
  }
  .card-art {
    position: absolute;
    inset: 0;
  }
  .brand {
    position: absolute;
    left: 250px;
    top: 120px;
  }
  .brand-name {
    font-family: "Exo 2", sans-serif;
    font-weight: 500;
    font-size: 92px;
    line-height: 1;
    letter-spacing: 2px;
    color: var(--title-blue);
    margin: 0;
  }
  .brand-tagline {
    font-size: 34px;
    color: var(--tag-blue);
    margin: 4px 0 0 4px;
  }
  .person-name {
    font-size: 32px;
    margin: 14px 0 0 4px;
  }
  .contact {
    position: absolute;
    top: 370px;
    font-size: 21px;
    line-height: 36px;
    white-space: nowrap;
  }
  .contact-direct { left: 250px; }
  .contact-web { left: 604px; }
  .contact-row {
    display: flex;
    align-items: center;
    gap: 12px;
  }
  .contact-row svg { width: 18px; height: 18px; flex: none; }
  .address-line { padding-left: 30px; }
  .divider {
    position: absolute;
    left: 580px;
    top: 350px;
    width: 1.5px;
    height: 170px;
    background: var(--ink);
  }
</style>
</head>
<body>
  <div class="business-card">
    <svg class="card-art" viewBox="0 0 1000 580" preserveAspectRatio="none">
      <defs>
        <radialGradient id="moonTone" cx="45%" cy="40%" r="60%">
          <stop offset="0%" stop-color="var(--moon-light)"/>
          <stop offset="100%" stop-color="var(--moon-shade)"/>
        </radialGradient>
      </defs>
      <rect width="1000" height="580" fill="var(--band-light)"/>
      <ellipse cx="500" cy="290" rx="478" ry="560" fill="var(--band-dark)"/>
      <ellipse cx="500" cy="290" rx="462" ry="548" fill="var(--band-mid)"/>
      <ellipse cx="500" cy="290" rx="448" ry="538" fill="var(--card-white)"/>
      <circle cx="500" cy="290" r="420" fill="url(#moonTone)" role="img" aria-label="Full moon photograph filling the card centre"/>
    </svg>

    <div class="brand">
      <p class="brand-name">KESTREL</p>
      <div class="brand-tagline">Yield Consulting</div>
      <div class="person-name">Desmond R Hale</div>
    </div>

    <div class="contact contact-direct">
      <div class="contact-row">
        <svg viewBox="0 0 18 18"><rect x="2" y="3" width="14" height="12" rx="1" fill="none" stroke="var(--icon-blue)" stroke-width="1.6"/><line x1="2" y1="7" x2="16" y2="7" stroke="var(--icon-blue)" stroke-width="1.6"/></svg>
        <span>(415) 555-0182</span>
      </div>
      <div class="contact-row">
        <svg viewBox="0 0 18 18"><path d="M4 2 L7 2 L8 6 L6 7.5 Q8 11 10.5 12 L12 10 L16 11 L16 14 Q10 16 5 10 Q2 6 4 2 Z" fill="var(--icon-blue)"/></svg>
        <span>(415) 555-0182</span>
      </div>
      <div class="contact-row">
        <svg viewBox="0 0 18 18"><rect x="1.5" y="4" width="15" height="10" fill="var(--icon-blue)"/><polyline points="1.5,4 9,10 16.5,4" fill="none" stroke="#fff" stroke-width="1.4"/></svg>
        <span>desmond@kestrelyield.com</span>
      </div>
    </div>

    <div class="divider"></div>

    <div class="contact contact-web">
      <div class="contact-row">
        <svg viewBox="0 0 18 18"><circle cx="9" cy="9" r="7.5" fill="none" stroke="var(--icon-blue)" stroke-width="1.5"/><ellipse cx="9" cy="9" rx="3.2" ry="7.5" fill="none" stroke="var(--icon-blue)" stroke-width="1.2"/><line x1="1.5" y1="9" x2="16.5" y2="9" stroke="var(--icon-blue)" stroke-width="1.2"/></svg>
        <span>www.kestrelyield.com</span>
      </div>
      <div class="contact-row">
        <svg viewBox="0 0 18 18"><path d="M9 17 Q3 10 3 7 A6 6 0 0 1 15 7 Q15 10 9 17 Z" fill="var(--icon-blue)"/><circle cx="9" cy="7" r="2.2" fill="#fff"/></svg>
        <span>418 Harbor Lane,</span>
      </div>
      <div class="contact-row address-line">
        <span>Alder Falls Oregon 97420</span>
      </div>
    </div>
  </div>
</body>
</html>
```